Flyer-Design für Kanutouristiker (Kanu Vermietung) Folgeaufträge!!
Zielgruppe
Wir veranstalten Kanu - und Erlebnistouren. Vermieten Kanus, Schlauchboote (Rafts), SUP (Stand up Paddling) und Fahrräder.
Für Gruppen, Betriebe, Schulklassen, Vereine, Familien, Junggesellenabschiede, Geburtstage usw.
Aufgabenstellung
Wir möchten einen ansprechenden Flyer erstellen lassen, der Lust auf unsere Angebote machen soll.
Hier handelt es sich um einen DIN lang (A4) Wickelfalz Falter (6 Seiter)
Mit unseren Angeboten. Beispielbilder sind im Anhang mithochgeladen. Es können weitere geliefert werden- oder Sie sehen sich einmal auf unserer Webseite um.
Wenig Text- lassen Sie die Bilder sprechen!!
Der Flyer soll lust auf eine Tour bei uns machen!
Der Flyer soll natürlich wirken.
Unsere CI wird schon durch unser Logo mitgegeben- es müssen nicht unbeding gr. Flächen mit unseren Farben gefüllt werden!!
Uns sprechen filigrane, künstlerische Designs an. Aber bitte die natürlichkeit nicht aus den Augen verlieren. Wir sind OUTDOORveranstalter- unsere Aktionen finden in der Natur statt!
Eine Variante, die ich aus zahlreichen Designs erarbeitet habe:
Nutzen Sie ein grosses Bild als Header (Kopfzeile) das auch z.B. im Orangeton (Logofarbe) überzeichnet - oder auch nur weiss (milchig) verändert sein darf.
Hierauf einen geeigneten Sinnspruch (Überschrift) z.B. "..mehr als nur ein Abenteuer"
der passend sein muss.
Etwas Poetisches vielleicht.... kurz und prägnant. (Natur, ökologie, Wasser, reisen...).
Bilder groß und darauf überlagert kleinere eingefasst in Rahmen.
Zum Textinhalt
Titelseite:
was machen wir?
Paddel- & Radtouren im Weser-Leinebergland, tolles Bild und unser Logo
evtl. noch für wen geeignet?
Schulklassen, Betriebe, Vereine, Familien, Junggesellenabschiede etc.
Innenseite(n):
Bilder, Bilder, Bilder (vielleicht gr. Hintergrundbild, dann kleine Bilder drauf mit passender Überschrift: z.B. Abenteuer im Talflitzer, Stand up paddling, Teambuilding Flossbau, Radverleih, Ruder & Räder, usw.
Rückseite:
Unsere Kontaktdaten
Firmenname
Webseite
Mailadresse
Hausanschrift
facebook
QR Code
LOGO
Toll wäre ein..

```html
<!DOCTYPE html>
<html lang="de">
<head>
<meta charset="utf-8">
<title>Talwelle Kanutouristik – Wickelfalz-Flyer</title>
<link rel="stylesheet" href="https://fonts.googleapis.com/css2?family=Kaushan+Script&family=Open+Sans:wght@400;600;700&family=Raleway:wght@300;400&display=swap">
<style>
  :root {
    --backdrop: #444444;
    --paper: #ffffff;
    --brand-red: #c4161c;
    --brand-orange: #f39200;
    --text-grey: #3c3c3c;
    --script: "Kaushan Script", cursive;
    --sans: "Open Sans", sans-serif;
    --body: "Raleway", sans-serif;
  }
  * { margin: 0; padding: 0; box-sizing: border-box; }
  html, body { width: 800px; height: 1200px; overflow: hidden; background: var(--backdrop); }
  .canvas { position: relative; width: 800px; height: 1200px; }

  .sheet { position: absolute; left: 21.5px; width: 762px; background: var(--paper); overflow: hidden; }
  .sheet--outside { top: 42px; height: 544px; }
  .sheet--inside { top: 600px; height: 533px; }
  .sheet svg.sheet-art { position: absolute; left: 0; top: 0; }

  .panel-copy { position: absolute; width: 220px; }
  .panel-title { font-family: var(--script); font-weight: 400; color: var(--brand-red); font-size: 25px; line-height: 1; letter-spacing: -0.5px; }
  .panel-sub { font-family: var(--script); color: var(--brand-orange); font-size: 11.5px; line-height: 1.2; margin-top: 3px; }
  .panel-text { font-family: var(--body); font-weight: 300; color: var(--text-grey); font-size: 10.2px; line-height: 13px; margin-top: 12px; }
  .offer-list { list-style: none; margin-top: 10px; font-family: var(--body); font-weight: 300; color: var(--text-grey); font-size: 10.2px; line-height: 13px; }
  .offer-list li { position: relative; padding-left: 16px; margin-bottom: 3.6px; }
  .offer-list li::before { content: ""; position: absolute; left: 2px; top: 5px; width: 3px; height: 3px; border-radius: 50%; background: #222; }

  .brand-mark { position: absolute; display: flex; align-items: center; gap: 6px; font-family: var(--sans); font-weight: 600; }
  .brand-mark .dot { border-radius: 50%; flex: none; }
  .brand-mark--cover { left: 562px; top: 82px; font-size: 26px; color: var(--brand-orange); }
  .brand-mark--cover .dot { width: 22px; height: 22px; background: var(--brand-orange); }
  .brand-mark--back { left: 338px; top: 239px; font-size: 17px; color: #fff; }
  .brand-mark--back .dot { width: 15px; height: 15px; background: #fff; }

  .contact { position: absolute; left: 275.5px; top: 302px; width: 254px; text-align: center; color: #fff; font-family: var(--sans); font-size: 7px; line-height: 9.5px; font-style: normal; }
  .contact .company { font-weight: 700; letter-spacing: 0.4px; margin-bottom: 6px; }
  .contact p + p { margin-top: 5px; }

  .cover-claim { position: absolute; left: 612px; top: 470px; font-family: var(--sans); font-weight: 700; line-height: 1; letter-spacing: 1px; }
  .cover-claim span { display: block; }
  .cover-claim .l1 { color: var(--brand-orange); font-size: 27px; }
  .cover-claim .l2 { color: var(--brand-red); font-size: 36px; margin-top: -2px; }
  .cover-claim .l3 { color: var(--brand-orange); font-size: 27px; margin-top: -1px; }

  .voucher-ribbon { position: absolute; left: 28px; top: 612px; width: 170px; height: 40px; }
  .voucher-ribbon .ribbon-title { position: absolute; left: 10px; top: 5px; font-family: var(--script); color: var(--brand-orange); font-size: 14px; transform: rotate(-3deg); }
  .voucher-ribbon .ribbon-sub { position: absolute; left: 54px; top: 23px; font-family: var(--script); color: #fff; font-size: 6.5px; transform: rotate(-3deg); }
</style>
</head>
<body>
<div class="canvas">

  <!-- Aussenseite: Innenklappe, Rückseite, Titel -->
  <section class="sheet sheet--outside">
    <svg class="sheet-art" width="762" height="544" viewBox="0 0 762 544">
      <defs>
        <path id="photo-panel" d="M0,0 H254 V336 C180,335 110,330 60,312 C36,300 40,292 70,285 C50,282 20,284 0,290 Z"/>
        <linearGradient id="g-business" x1="0" y1="0" x2="0" y2="1">
          <stop offset="0" stop-color="#eef1f3"/><stop offset="0.35" stop-color="#c9ccd0"/><stop offset="0.7" stop-color="#8d8f94"/><stop offset="1" stop-color="#d6d8da"/>
        </linearGradient>
        <radialGradient id="g-business-suits" cx="0.55" cy="0.6" r="0.55">
          <stop offset="0" stop-color="#2f3136" stop-opacity="0.75"/><stop offset="0.6" stop-color="#55585f" stop-opacity="0.4"/><stop offset="1" stop-color="#55585f" stop-opacity="0"/>
        </radialGradient>
        <radialGradient id="g-business-light" cx="0.2" cy="0.45" r="0.35">
          <stop offset="0" stop-color="#b59f86" stop-opacity="0.55"/><stop offset="1" stop-color="#b59f86" stop-opacity="0"/>
        </radialGradient>
        <linearGradient id="g-raft" x1="0" y1="0" x2="0" y2="1">
          <stop offset="0" stop-color="#4f7a34"/><stop offset="0.22" stop-color="#8bb35a"/><stop offset="0.36" stop-color="#b8ab98"/><stop offset="0.5" stop-color="#8e9a94"/><stop offset="0.78" stop-color="#3a2a2c"/><stop offset="1" stop-color="#7a2624"/>
        </linearGradient>
        <radialGradient id="g-raft-crew" cx="0.5" cy="0.62" r="0.5">
          <stop offset="0" stop-color="#d8403a" stop-opacity="0.85"/><stop offset="0.55" stop-color="#b63a3a" stop-opacity="0.45"/><stop offset="1" stop-color="#b63a3a" stop-opacity="0"/>
        </radialGradient>
        <radialGradient id="g-raft-glow" cx="0.6" cy="0.45" r="0.3">
          <stop offset="0" stop-color="#e8c3a2" stop-opacity="0.6"/><stop offset="1" stop-color="#e8c3a2" stop-opacity="0"/>
        </radialGradient>
      </defs>

      <g role="img" aria-label="Foto: Team in Businesskleidung im hellen Büroflur">
        <use href="#photo-panel" fill="url(#g-business)"/>
        <use href="#photo-panel" fill="url(#g-business-suits)"/>
        <use href="#photo-panel" fill="url(#g-business-light)"/>
      </g>
      <path fill="var(--brand-orange)"
            d="M14,305 C8,290 40,282 70,285 C40,292 36,300 60,312 C110,330 180,335 254,336 L254,358 C170,356 80,345 35,328 C20,322 16,314 14,305 Z"/>

      <path fill="var(--brand-red)"
            d="M254,16 C320,10 380,12 384,24 C388,38 306,38 306,58 C306,80 420,96 762,125 L762,543 L254,543 Z"/>

      <g role="img" aria-label="Foto: jubelnde Gruppe mit erhobenen Paddeln im roten Schlauchboot auf dem Fluss">
        <rect x="508" y="138" width="254" height="406" fill="url(#g-raft)"/>
        <rect x="508" y="138" width="254" height="406" fill="url(#g-raft-crew)"/>
        <rect x="508" y="138" width="254" height="406" fill="url(#g-raft-glow)"/>
      </g>
      <path fill="var(--brand-orange)"
            d="M254,14 C320,6 385,6 390,22 C394,40 314,38 314,58 C314,78 430,92 762,118 L762,154 C600,140 420,118 330,88 C306,78 300,68 300,58 C300,36 378,36 376,24 C372,14 320,16 254,18 Z"/>
    </svg>

    <div class="panel-copy" style="left:25px; top:371px;">
      <h2 class="panel-title">Planen Sie mit uns</h2>
      <p class="panel-sub">Ihren nächsten Betriebsausflug!</p>
      <p class="panel-text">Spass, Team Zusammenhalt und eine neue Herausforderung - all das bietet Ihnen Talwelle.</p>
    </div>
  </section>

  <div class="brand-mark brand-mark--back"><span class="dot"></span>talwelle.de</div>
  <address class="contact">
    <p class="company">TALWELLE<br>KANUTOURISTIK</p>
    <p>Lena Hartwig<br>37699 Brückenau (Talhausen/Weser)</p>
    <p>Tel.:&nbsp;&nbsp; 0 55 00 - 12 34 56<br>Mobil: 0 15 00 - 11 22 333</p>
  </address>

  <div class="brand-mark brand-mark--cover"><span class="dot"></span>talwelle.de</div>
  <h1 class="cover-claim"><span class="l1">AUF DEM</span><span class="l2">WASSER</span><span class="l3">ZU HAUSE.</span></h1>

  <!-- Innenseite: drei Angebotsspalten -->
  <section class="sheet sheet--inside">
    <svg class="sheet-art" width="762" height="533" viewBox="0 0 762 533">
      <defs>
        <path id="offer-photo" d="M0,0 H254 V336 C180,335 110,330 60,312 C36,300 40,292 70,285 C50,282 20,284 0,290 Z"/>
        <path id="wave-band" d="M14,305 C8,290 40,282 70,285 C40,292 36,300 60,312 C110,330 180,335 254,336 L254,358 C170,356 80,345 35,328 C20,322 16,314 14,305 Z"/>

        <linearGradient id="g-canoe" x1="0" y1="0" x2="0" y2="1">
          <stop offset="0" stop-color="#5ea6ea"/><stop offset="0.18" stop-color="#9cc8ee"/><stop offset="0.3" stop-color="#5f8f3c"/><stop offset="0.6" stop-color="#3e6b2a"/><stop offset="0.72" stop-color="#6a8a4a"/><stop offset="0.85" stop-color="#c4262b"/><stop offset="1" stop-color="#8c2a26"/>
        </linearGradient>
        <radialGradient id="g-canoe-wall" cx="0.92" cy="0.28" r="0.35">
          <stop offset="0" stop-color="#b8916a" stop-opacity="0.85"/><stop offset="1" stop-color="#b8916a" stop-opacity="0"/>
        </radialGradient>
        <radialGradient id="g-canoe-crew" cx="0.55" cy="0.8" r="0.45">
          <stop offset="0" stop-color="#e04a44" stop-opacity="0.6"/><stop offset="1" stop-color="#e04a44" stop-opacity="0"/>
        </radialGradient>

        <linearGradient id="g-rafting" x1="0" y1="0" x2="0" y2="1">
          <stop offset="0" stop-color="#6f8e98"/><stop offset="0.3" stop-color="#8aa3a8"/><stop offset="0.55" stop-color="#9aa4a0"/><stop offset="0.85" stop-color="#c23a32"/><stop offset="1" stop-color="#e05a4c"/>
        </linearGradient>
        <radialGradient id="g-rafting-helmets" cx="0.5" cy="0.42" r="0.45">
          <stop offset="0" stop-color="#f2d23c" stop-opacity="0.85"/><stop offset="0.6" stop-color="#e0b830" stop-opacity="0.35"/><stop offset="1" stop-color="#e0b830" stop-opacity="0"/>
        </radialGradient>
        <radialGradient id="g-rafting-vests" cx="0.45" cy="0.68" r="0.4">
          <stop offset="0" stop-color="#c8282a" stop-opacity="0.75"/><stop offset="1" stop-color="#c8282a" stop-opacity="0"/>
        </radialGradient>

        <linearGradient id="g-bikes" x1="0" y1="0" x2="0" y2="1">
          <stop offset="0" stop-color="#b6d8ef"/><stop offset="0.2" stop-color="#d9ebf4"/><stop offset="0.3" stop-color="#3f6f34"/><stop offset="0.48" stop-color="#6c9a45"/><stop offset="0.72" stop-color="#9fc266"/><stop offset="0.85" stop-color="#c9cfc6"/><stop offset="1" stop-color="#a6c86a"/>
        </linearGradient>
        <radialGradient id="g-bikes-riders" cx="0.55" cy="0.62" r="0.4">
          <stop offset="0" stop-color="#d85a8a" stop-opacity="0.45"/><stop offset="0.5" stop-color="#5b8ed0" stop-opacity="0.25"/><stop offset="1" stop-color="#5b8ed0" stop-opacity="0"/>
        </radialGradient>
      </defs>

      <g role="img" aria-label="Foto: Kanu mit vier Paddlerinnen vor Burgmauer am Flussufer">
        <use href="#offer-photo" fill="url(#g-canoe)"/>
        <use href="#offer-photo" fill="url(#g-canoe-wall)"/>
        <use href="#offer-photo" fill="url(#g-canoe-crew)"/>
      </g>
      <use href="#wave-band" fill="var(--brand-orange)"/>

      <g transform="translate(254,0)">
        <g role="img" aria-label="Foto: Gruppe mit gelben Helmen und Paddeln im Schlauchboot im Wildwasser">
          <use href="#offer-photo" fill="url(#g-rafting)"/>
          <use href="#offer-photo" fill="url(#g-rafting-helmets)"/>
          <use href="#offer-photo" fill="url(#g-rafting-vests)"/>
        </g>
        <use href="#wave-band" fill="var(--brand-orange)"/>
      </g>

      <g transform="translate(508,0)">
        <g role="img" aria-label="Foto: Familie auf Fahrrädern auf einem Weg durch grüne Hügellandschaft">
          <use href="#offer-photo" fill="url(#g-bikes)"/>
          <use href="#offer-photo" fill="url(#g-bikes-riders)"/>
        </g>
        <use href="#wave-band" fill="var(--brand-orange)"/>
      </g>
    </svg>

    <div class="panel-copy" style="left:25px; top:370px;">
      <h2 class="panel-title">Kanutouren</h2>
      <p class="panel-sub">Natur pur im Weser- und Leinebergland</p>
      <ul class="offer-list">
        <li>Paddeltouren an der Weser</li>
        <li>Paddeltouren an der Leine</li>
      </ul>
    </div>
    <div class="panel-copy" style="left:279px; top:370px;">
      <h2 class="panel-title">Schlauchboote</h2>
      <p class="panel-sub">… Kentern ausgeschlossen!</p>
      <ul class="offer-list">
        <li>Touren auf der Weser und der Leine</li>
        <li>Raftboote mit bis zu 12 Personen</li>
        <li>Einfache Handhabung und bequeme Sitzposition</li>
      </ul>
    </div>
    <div class="panel-copy" style="left:533px; top:370px;">
      <h2 class="panel-title">Allerlei Vielfalt…</h2>
      <p class="panel-sub">Da ist für jeden was dabei!</p>
      <ul class="offer-list">
        <li>Bogenschiessen</li>
        <li>Radfahren</li>
        <li>Stand up Paddeling</li>
        <li>Für Schulklassen: das schwimmende Klassenzimmer</li>
        <li>Teambuilding Flossbau</li>
      </ul>
    </div>
  </section>

  <div class="voucher-ribbon">
    <svg width="170" height="40" viewBox="0 0 170 40">
      <path d="M4,8 L168,0 L160,20 L168,30 L8,38 L2,26 Z" fill="var(--brand-red)"/>
    </svg>
    <span class="ribbon-title">Geschenkgutscheine</span>
    <span class="ribbon-sub">Verschenken Sie doch mal eine Paddeltour!</span>
  </div>

</div>
</body>
</html>
```